Business Card design for insurance broker in Denver, CO, USA

I need a business card designed using this logo that was just created. We sell life and disability income insurance to US consumers.
Looking for a professionally designed card to make use of the logo and have something to hand to prospects or new business referral sources. The card could be white, gray, black or whatever you would recommend.

Target Market(s)

US Consumers and other financial professionals that I partner with.

Industry/Entity Type

Insurance Broker

Contact Information for Business Card

Owen R. Tessler, CLU, LUTCF (please note that CLU should have a superscript R in a circle for registered trademark)
President
phone (303) 555-0147
email owen@brightlakecoverage.com
4620 W. Hollister Rd, Suite 310, Greenwood Village, CO 80111
Somewhere fit in a tagline saying "Your resource for life, long term care, and disability insurance" (maybe the back if it doesn't fit on the front, your call)

Font styles to use
Sans Serif

Requirements
Must have
• Must have logo in correct blue and gray colors, my name, address, phone, email. Order and placement determined by the designer.
• I just want something that looks a more professional than what I could have done using the business card designer tool on printmakerhub.com or CardNest, or any other do-it-yourself tool
• A regular rectangular business card with square corners is preferred
Nice to have
• I included the logos of 2 organizations I belong to (GQLF and BEPWO). They should be small, but visible on the back only. If it doesn’t look good, this is not a requirement, feel free to drop it.
Should not have
• Do not add any colors not already in the logo, except use of black and whites which are okay. If you use the logo on the back and want to make that in all black, gray or white, that may be okay as well.

```html
<!DOCTYPE html>
<html lang="en">
<head>
<meta charset="utf-8">
<title>Brightlake Coverage – Business Card</title>
<link rel="stylesheet" href="https://fonts.googleapis.com/css2?family=Lato:wght@400;700&display=swap">
<style>
  :root {
    --brand-blue: #2288cc;
    --text-gray: #999999;
    --card-white: #ffffff;
    --backdrop: #a6a6a6;
    --watermark-blue: #d9eaf6;
    --watermark-gray: #eeeeee;
  }
  html, body {
    margin: 0;
    padding: 0;
    width: 1200px;
    height: 930px;
    overflow: hidden;
  }
  body {
    background: var(--backdrop);
    font-family: "Lato", Arial, sans-serif;
    position: relative;
  }
  .card {
    position: absolute;
    width: 560px;
    height: 320px;
    border-radius: 18px;
    box-shadow: 0 8px 20px rgba(0,0,0,0.2);
    overflow: hidden;
  }
  .card--front {
    left: 90px;
    top: 110px;
    background: var(--brand-blue);
    color: var(--card-white);
  }
  .card--back {
    left: 550px;
    top: 500px;
    background: var(--card-white);
  }
  .brand {
    position: absolute;
    display: flex;
    align-items: center;
    gap: 14px;
  }
  .brand__dot {
    border-radius: 50%;
    border: 4px solid currentColor;
    box-sizing: border-box;
    flex: none;
  }
  .brand__name {
    font-weight: 700;
    text-transform: uppercase;
    line-height: 0.95;
    letter-spacing: 1px;
  }
  .card--front .brand {
    left: 0;
    right: 0;
    top: 108px;
    justify-content: center;
    color: var(--card-white);
  }
  .card--front .brand__dot { width: 74px; height: 74px; }
  .card--front .brand__name { font-size: 34px; }
  .tagline {
    position: absolute;
    left: 0;
    right: 0;
    bottom: 22px;
    margin: 0;
    text-align: center;
    font-size: 11.5px;
    letter-spacing: 0.6px;
    text-transform: uppercase;
  }
  .card--back .brand {
    right: 26px;
    top: 26px;
    color: var(--brand-blue);
  }
  .card--back .brand__dot { width: 46px; height: 46px; border-width: 3px; }
  .card--back .brand__name { font-size: 20px; }
  .watermark {
    position: absolute;
    left: 80px;
    top: 70px;
    width: 300px;
    height: 300px;
  }
  .holder {
    position: absolute;
    left: 30px;
    top: 150px;
  }
  .holder__name {
    margin: 0;
    font-size: 20px;
    font-weight: 700;
    color: var(--brand-blue);
  }
  .holder__name sup { font-size: 9px; }
  .holder__title {
    margin: 2px 0 0;
    font-size: 15px;
    color: var(--text-gray);
  }
  .contact {
    position: absolute;
    left: 30px;
    bottom: 26px;
    margin: 0;
    padding: 0;
    list-style: none;
    font-size: 15px;
    color: var(--text-gray);
  }
  .contact li {
    display: flex;
    align-items: center;
    gap: 8px;
    margin-top: 4px;
  }
  .contact svg { width: 12px; height: 12px; fill: var(--brand-blue); }
  .address {
    position: absolute;
    right: 26px;
    bottom: 64px;
    margin: 0;
    text-align: right;
    font-style: normal;
    font-size: 15px;
    line-height: 1.35;
    color: var(--text-gray);
  }
</style>
</head>
<body>

<section class="card card--front" aria-label="Card front">
  <div class="brand">
    <span class="brand__dot"></span>
    <span class="brand__name">Brightlake<br>Coverage</span>
  </div>
  <p class="tagline">Your resource for life, long term care, and disability insurance</p>
</section>

<section class="card card--back" aria-label="Card back">
  <svg class="watermark" viewBox="0 0 300 300" aria-hidden="true">
    <path d="M150 10 A140 140 0 0 1 290 150" fill="none" stroke="var(--watermark-gray)" stroke-width="10"/>
    <path d="M290 150 A140 140 0 1 1 150 10" fill="none" stroke="var(--watermark-blue)" stroke-width="10"/>
  </svg>

  <div class="brand">
    <span class="brand__dot"></span>
    <span class="brand__name">Brightlake<br>Coverage</span>
  </div>

  <div class="holder">
    <h1 class="holder__name">Owen R. Tessler, CLU<sup>®</sup>, LUTCF</h1>
    <p class="holder__title">President</p>
  </div>

  <ul class="contact">
    <li>
      <svg viewBox="0 0 24 24" aria-hidden="true"><path d="M6.6 10.8a15.1 15.1 0 0 0 6.6 6.6l2.2-2.2a1 1 0 0 1 1-.25 11.4 11.4 0 0 0 3.6.6 1 1 0 0 1 1 1V20a1 1 0 0 1-1 1A17 17 0 0 1 3 4a1 1 0 0 1 1-1h3.5a1 1 0 0 1 1 1c0 1.250.2 2.45.6 3.6a1 1 0 0 1-.25 1z"/></svg>
      (303) 555-0147
    </li>
    <li>
      <svg viewBox="0 0 24 24" aria-hidden="true"><path d="M2 5h20v14H2zm2 2v.5l8 5 8-5V7zm0 2.8V17h16V9.8l-8 5z"/></svg>
      owen@brightlakecoverage.com
    </li>
  </ul>

  <address class="address">
    4620 W. Hollister Rd, Suite 310,<br>
    Maple Ridge, CO 80492
  </address>
</section>

</body>
</html>
```